App Design for Restaurant App

We need a design for the new Mobile App for the Restaurant Volmik. See attachment for presentation sketches.
There are two attached files: File 2 shows the App in general and File 1 shows the five screens which need to be designed. Your work should contain the general color scheme, icons and layout proposal.
Updates
Hi Designers
There where several questions about the scope of the work. We are looking for a design for an App. The promotion website of the restaurant Volmik can be found under www.restaurant-volmik.ch
There you will get an impression of the Corporate Identity used by the restaurant and you will also find the logo.
In the sketch there are several screens which don't need a design, e.g. the cover flow or video screen
please ask if you have any question
kind regards
Tobias
Industry/Entity Type
Restaurant
Look and feel
Each slider illustrates characteristics of the customer's brand and the style your logo design should communicate.

```html
<!DOCTYPE html>
<html lang="de">
<head>
<meta charset="utf-8">
<title>Restaurant Volmik – Events</title>
<link href="https://fonts.googleapis.com/css2?family=Signika:wght@600;700&display=swap" rel="stylesheet">
<style>
  :root{
    --stage:#1c1c1c;
    --cream:#fdf9c6;
    --cream-text:#f8f4c4;
    --olive-light:#7a8a3c;
    --olive:#5a6a26;
    --olive-dark:#3c4812;
    --divider-dark:#2f3a0c;
    --divider-light:#7d8c45;
    --photo-red:#a8262a;
    --photo-warm:#c9a77a;
    --photo-dark:#4a3a2e;
  }
  *{box-sizing:border-box;margin:0;padding:0}
  html,body{width:711px;height:1200px;overflow:hidden;background:var(--stage)}
  body{position:relative;font-family:"Signika",Arial,sans-serif}
  .screen{
    position:absolute;left:116px;top:222px;width:486px;height:731px;
    background:var(--cream);overflow:hidden;
  }
  .nav-bar{
    position:absolute;left:0;top:0;width:100%;height:79px;
    background:linear-gradient(180deg,var(--olive-light) 0%,var(--olive) 45%,var(--olive-dark) 100%);
    border-bottom:1px solid var(--divider-dark);
  }
  .back-button{
    position:absolute;left:14px;top:20px;width:74px;height:37px;
  }
  .back-button svg{position:absolute;inset:0}
  .back-button span{
    position:absolute;left:15px;top:7px;font-weight:700;font-size:17px;color:var(--olive-dark);
  }
  .nav-title{
    position:absolute;left:0;right:0;top:21px;text-align:center;
    font-weight:700;font-size:27px;color:#fff;letter-spacing:-0.3px;
    text-shadow:0 1px 1px rgba(0,0,0,.4);
  }
  .menu-icon{position:absolute;right:28px;top:32px}
  .hero{
    position:absolute;left:0;top:80px;width:100%;height:200px;
    background:
      linear-gradient(180deg,rgba(60,45,35,.55) 0%,rgba(0,0,0,0) 35%,rgba(0,0,0,0) 60%,rgba(90,40,30,.35) 100%),
      linear-gradient(90deg,var(--photo-warm) 0%,var(--photo-red) 30%,#e8e0d4 50%,var(--photo-red) 72%,var(--photo-dark) 100%);
  }
  .brand-tile{
    position:absolute;left:188px;top:80px;width:124px;height:95px;background:#fdf8c8;
    display:flex;align-items:center;justify-content:center;text-align:center;
  }
  .brand-tile span{font-weight:600;font-size:13px;color:#3a3a1e;letter-spacing:1px;line-height:1.3;text-transform:uppercase}
  .event-list{
    position:absolute;left:27px;top:326px;width:433px;height:280px;
    border-radius:8px;border:1px solid var(--divider-dark);overflow:hidden;
    background:linear-gradient(180deg,var(--olive) 0%,var(--olive-dark) 100%);
    list-style:none;box-shadow:0 1px 2px rgba(0,0,0,.3);
  }
  .event-item{
    position:relative;height:66px;display:flex;align-items:center;
    border-bottom:1px solid var(--divider-dark);box-shadow:0 1px 0 var(--divider-light);
    background:linear-gradient(180deg,rgba(255,255,255,.06),rgba(0,0,0,.08));
  }
  .event-item:first-child{height:74px}
  .event-item:last-child{border-bottom:none;box-shadow:none;flex:1;height:70px}
  .event-item .plus{position:absolute;left:22px}
  .event-item .label{position:absolute;left:76px;font-weight:600;font-size:23px;color:var(--cream-text);letter-spacing:-0.3px}
  .event-item .chevron{position:absolute;right:45px}
</style>
</head>
<body>
<main class="screen">
  <header class="nav-bar">
    <a class="back-button" aria-label="Zurück">
      <svg width="74" height="37" viewBox="0 0 74 37"><path d="M14 1H69a4 4 0 0 1 4 4v27a4 4 0 0 1-4 4H14L1 18.5Z" fill="#fdf9c6" stroke="#3c4812"/></svg>
      <span>Zuruck</span>
    </a>
    <h1 class="nav-title">Events</h1>
    <svg class="menu-icon" width="24" height="24" viewBox="0 0 24 24" aria-label="Menü"><g fill="#fff"><rect x="0" y="0" width="10.5" height="10.5"/><rect x="13.5" y="0" width="10.5" height="10.5"/><rect x="0" y="13.5" width="10.5" height="10.5"/><rect x="13.5" y="13.5" width="10.5" height="10.5"/></g></svg>
  </header>
  <div class="hero" role="img" aria-label="Festlich gedeckter Restaurantsaal mit roten Stuhlhussen und Weihnachtsdekoration"></div>
  <div class="brand-tile"><span>Restaurant<br>Volmik</span></div>
  <ul class="event-list">
    <li class="event-item">
      <svg class="plus" width="26" height="26" viewBox="0 0 26 26"><circle cx="13" cy="13" r="13" fill="#2a330a"/><path d="M13 7v12M7 13h12" stroke="#fff" stroke-width="3"/></svg>
      <span class="label">Auto-Kino</span>
      <svg class="chevron" width="9" height="14" viewBox="0 0 9 14"><path d="M1.5 1.5l6 5.5-6 5.5" fill="none" stroke="#fff" stroke-width="1.8"/></svg>
    </li>
    <li class="event-item">
      <svg class="plus" width="26" height="26" viewBox="0 0 26 26"><circle cx="13" cy="13" r="13" fill="#2a330a"/><path d="M13 7v12M7 13h12" stroke="#fff" stroke-width="3"/></svg>
      <span class="label">September - Oktober</span>
      <svg class="chevron" width="9" height="14" viewBox="0 0 9 14"><path d="M1.5 1.5l6 5.5-6 5.5" fill="none" stroke="#fff" stroke-width="1.8"/></svg>
    </li>
    <li class="event-item">
      <svg class="plus" width="26" height="26" viewBox="0 0 26 26"><circle cx="13" cy="13" r="13" fill="#2a330a"/><path d="M13 7v12M7 13h12" stroke="#fff" stroke-width="3"/></svg>
      <span class="label">Oktober - November</span>
      <svg class="chevron" width="9" height="14" viewBox="0 0 9 14"><path d="M1.5 1.5l6 5.5-6 5.5" fill="none" stroke="#fff" stroke-width="1.8"/></svg>
    </li>
    <li class="event-item">
      <svg class="plus" width="26" height="26" viewBox="0 0 26 26"><circle cx="13" cy="13" r="13" fill="#2a330a"/><path d="M13 7v12M7 13h12" stroke="#fff" stroke-width="3"/></svg>
      <span class="label">31.Dezember 2012</span>
      <svg class="chevron" width="9" height="14" viewBox="0 0 9 14"><path d="M1.5 1.5l6 5.5-6 5.5" fill="none" stroke="#fff" stroke-width="1.8"/></svg>
    </li>
  </ul>
</main>
</body>
</html>
```